Need a sleek, professional business card design for a Web Development business

I need a unique business card designed for a web development company. It is also the parent company for any ventures I do, such as my ClipHarbor channel, startup ideas I have, etc. I am the single member of "Copper Lantern Sites LLC." I will attach my basic logo here, so you will see the current color scheme and have the asset available. Thank you!

Target Market(s)

Startups, SMB's, Professionals

Industry/Entity Type

Business

Font styles to use
Other font styles liked:
• Lovello for headings is what I use, but not necessary.

Colors

Designer to choose colors to be used in the design.

Requirements
Nice to have
• Sleek is the word. Professional, modern, dark.
Should not have
• Any work from someone else's design. Lacking originality.

```html
<!DOCTYPE html>
<html lang="en">
<head>
<meta charset="utf-8">
<title>Copper Lantern Sites – Business Card</title>
<link rel="stylesheet" href="https://fonts.googleapis.com/css2?family=Oswald:wght@600&family=Lato:wght@400;700&display=swap">
<style>
  :root {
    --page-bg: #3b4048;
    --card-top: #3a3a3c;
    --card-bottom: #1f1f21;
    --accent: #f0784a;
    --text-light: #ececec;
    --text-muted: #bdbdbd;
    --brand-grey: #8a8a8c;
  }
  * { margin: 0; padding: 0; box-sizing: border-box; }
  html, body { width: 1200px; height: 900px; overflow: hidden; }
  body {
    background: var(--page-bg);
    display: flex;
    align-items: center;
    justify-content: center;
    gap: 60px;
    font-family: "Lato", sans-serif;
  }
  .card {
    width: 520px;
    height: 297px;
    border-radius: 4px;
    background: linear-gradient(135deg, var(--card-top), var(--card-bottom));
    box-shadow: 0 18px 40px rgba(0,0,0,.45);
    position: relative;
    overflow: hidden;
  }
  /* front */
  .card-front { display: flex; align-items: center; }
  .identity {
    width: 236px;
    text-align: right;
    padding-right: 24px;
  }
  .identity-name {
    font-family: "Oswald", sans-serif;
    font-weight: 600;
    font-size: 38px;
    line-height: 1;
    letter-spacing: .5px;
    color: var(--accent);
    text-transform: uppercase;
  }
  .identity-role {
    margin-top: 8px;
    font-size: 15px;
    color: var(--text-muted);
  }
  .divider {
    width: 2px;
    height: 120px;
    background: var(--accent);
  }
  .contact {
    padding-left: 24px;
    font-size: 15px;
    line-height: 1.45;
    color: var(--text-light);
    list-style: none;
  }
  .contact-item { display: flex; align-items: center; gap: 9px; }
  .contact-item.address { padding-left: 23px; }
  .contact-icon { width: 14px; height: 14px; fill: var(--accent); flex: none; }
  /* back */
  .card-back {
    display: flex;
    flex-direction: column;
    align-items: center;
    justify-content: center;
    gap: 22px;
  }
  .brand {
    display: flex;
    align-items: center;
    gap: 12px;
    font-size: 26px;
    font-weight: 700;
    color: var(--brand-grey);
  }
  .brand-dot {
    width: 16px; height: 16px;
    border-radius: 50%;
    background: var(--brand-grey);
  }
  .back-url { font-size: 15px; color: var(--text-light); letter-spacing: .3px; }
</style>
</head>
<body>
  <section class="card card-front">
    <div class="identity">
      <h1 class="identity-name">Dean Harlow</h1>
      <p class="identity-role">Manager</p>
    </div>
    <div class="divider"></div>
    <ul class="contact">
      <li class="contact-item address">418 Birch Row</li>
      <li class="contact-item address">Austin, TX 78704</li>
      <li class="contact-item">
        <svg class="contact-icon" viewBox="0 0 16 16"><path d="M3.6 1.2l2.2 2.6-1.3 1.7c.9 2 2.5 3.6 4.6 4.6l1.6-1.3 2.7 2.2-1.3 2.2C6.5 13.9 1.9 9.4 1.5 2.6z"/></svg>
        512 555 0142
      </li>
      <li class="contact-item">
        <svg class="contact-icon" viewBox="0 0 16 16"><path d="M4 1h8v4H4zM1 6h14v6h-3v3H4v-3H1zm4 4v3h6v-3z"/></svg>
        512 555 0143
      </li>
      <li class="contact-item">
        <svg class="contact-icon" viewBox="0 0 16 16"><path d="M1 3h14v10H1zm1.5 1.5L8 9l5.5-4.5z" fill-rule="evenodd"/></svg>
        info@copperlanternsites.com
      </li>
      <li class="contact-item">
        <svg class="contact-icon" viewBox="0 0 16 16"><path d="M8 1a7 7 0 100 14A7 7 0 008 1zm-5.4 6h2.6c.1-1.6.5-3 1.1-4A5.6 5.6 0 002.6 7zm4 0h2.8C9.3 5 8.7 3.3 8 2.6 7.3 3.3 6.7 5 6.6 7zm4.2 0h2.6a5.6 5.6 0 00-3.7-4c.6 1 1 2.4 1.1 4zM2.6 9a5.6 5.6 0 003.7 4c-.6-1-1-2.4-1.1-4zm4 0c.1 2 .7 3.7 1.4 4.4.7-.7 1.3-2.4 1.4-4.4zm4.2 0c-.1 1.6-.5 3-1.1 4a5.6 5.6 0 003.7-4z"/></svg>
        www.copperlanternsites.com
      </li>
    </ul>
  </section>

  <section class="card card-back">
    <div class="brand"><span class="brand-dot"></span>Copper Lantern Sites</div>
    <p class="back-url">www.copperlanternsites.com</p>
  </section>
</body>
</html>
```